Website Design for Tarrowby & Quenell LLC

We are looking for a new website design for our law firm. We have provided links to other websites that we find appealing.

```html
<!DOCTYPE html>
<html lang="en">
<head>
<meta charset="utf-8">
<title>Tarrowby &amp; Quenell L.L.C.</title>
<link rel="stylesheet" href="https://fonts.googleapis.com/css2?family=Tinos:wght@400;700&display=swap">
<style>
:root{
  --page:#ffffff;
  --lime:#b9cf6d;
  --lime-pale:#d3e29a;
  --olive:#5a6e1c;
  --olive-dark:#4a5c14;
  --olive-mid:#6c8228;
  --nav-active:#627a1c;
  --head-text:#3a3a26;
  --title-green:#5a6e1c;
  --body-text:#333322;
  --cream:#eef2c6;
  --phone:#e4eb9a;
  --footer:#8fae3a;
  --hero-fill:#9db4a6;
  --project-fill:#a8a08a;
  --flag-fill:rgba(214,196,150,.28);
}
*{margin:0;padding:0;box-sizing:border-box}
html,body{width:1200px;height:869px;overflow:hidden;background:var(--page)}
body{font-family:"Tinos","Times New Roman",serif;position:relative}
.site{position:absolute;left:171px;top:4px;width:857px;height:860px;background:var(--lime)}
.masthead{position:absolute;left:0;top:0;width:857px;height:109px;background:linear-gradient(90deg,#aec45b 0%,#d6e49e 55%,#bcd06a 76%)}
.masthead .brand{position:absolute;left:64px;top:14px;font-size:37px;line-height:41px;color:var(--head-text);letter-spacing:.5px}
.masthead .corner{position:absolute;right:0;top:0;width:205px;height:109px;background:var(--olive-dark)}
.nav{position:absolute;left:0;top:109px;width:857px;height:36px;background:linear-gradient(#4f6314,#3a4a0c);display:flex;align-items:center;border-bottom:2px solid #a5bd52}
.nav a{color:#e9edc4;text-decoration:none;font-size:12px;font-weight:700;letter-spacing:.4px;height:100%;display:flex;align-items:center}
.nav a.active{background:var(--nav-active);color:#eef6a0;padding:0 17px;margin-left:50px}
.nav a.l2{margin-left:30px}.nav a.l3{margin-left:47px}.nav a.l4{margin-left:47px}
.hero{position:absolute;left:0;top:147px;width:857px;height:190px;background:var(--hero-fill)}
.projects{position:absolute;left:17px;top:356px;width:184px}
.project-photo{width:184px;height:117px;border:2px solid #6f7e3e;background:var(--project-fill)}
.caption{font-size:11.5px;font-weight:700;line-height:14px;text-align:center;color:var(--head-text);margin:3px 0 0;height:39px}
.clients{position:absolute;left:220px;top:353px;width:414px;height:455px;background:var(--lime-pale)}
.flag{position:absolute;left:20px;top:95px;width:370px;height:190px;background:var(--flag-fill)}
.clients h2{position:relative;font-size:17px;line-height:20px;color:var(--title-green);margin:12px 0 0 22px;font-weight:700}
.client-list{position:relative;list-style:none;margin:6px 0 0 36px}
.client-list li{font-size:14.5px;line-height:31.7px;color:var(--body-text)}
.services{position:relative;list-style:none;margin:10px 0 0 22px;width:385px}
.services li{font-size:12.5px;line-height:21px;color:var(--body-text);padding-left:14px;text-indent:-14px}
.services li::before{content:"* ";}
.sidebar{position:absolute;left:652px;top:337px;width:205px;height:488px;background:var(--olive)}
.tab{position:absolute;left:9px;width:188px;height:35px;background:var(--footer);color:#f4f6d8;font-weight:700;font-size:15px;letter-spacing:.5px;display:flex;align-items:center;justify-content:center}
.tab.areas{top:23px}.tab.offices{top:280px}
.practice{position:absolute;left:23px;top:62px;list-style:none}
.practice li{font-size:15px;line-height:26.7px;color:var(--cream)}
.office-box{position:absolute;left:9px;top:315px;width:188px;height:127px;background:var(--olive-mid);text-align:center}
.office-box .city{font-size:14px;color:var(--cream);letter-spacing:.3px}
.office-box .phone{font-size:21px;color:var(--phone)}
.c1{margin-top:9px}.c2{margin-top:14px}
.footer{position:absolute;left:0;top:825px;width:857px;height:35px;background:var(--footer);display:flex;align-items:center;justify-content:center;font-size:13px;color:var(--body-text);gap:12px}
.footer a{color:var(--body-text)}
</style>
</head>
<body>
<div class="site">
  <header class="masthead">
    <div class="brand">TARROWBY &amp;<br>QUENELL L.L.C.</div>
    <div class="corner"></div>
  </header>
  <nav class="nav">
    <a class="active" href="#">HOME</a>
    <a class="l2" href="#">ENVIRONMENTAL LAW</a>
    <a class="l3" href="#">LAND USE / COMPLEX LITIGATION</a>
    <a class="l4" href="#">CORPORATE LAW / TRANSACTIONS</a>
  </nav>
  <div class="hero" role="img" aria-label="Landscape photo: a calm lake edged by trees and reeds"></div>

  <aside class="projects">
    <div class="project-photo" role="img" aria-label="Project photo: residential building"></div>
    <p class="caption">Client Project: The Residences<br>at Harlow Square, Princeton</p>
    <div class="project-photo" role="img" aria-label="Project photo: redeveloped mid-rise building"></div>
    <p class="caption">Client Project: Redevelopment -<br>Institutional to Mixed Residential</p>
    <div class="project-photo" role="img" aria-label="Project photo: historic clubhouse"></div>
    <p class="caption">Client Project: Expansion of historic<br>Elmhurst Club of Princeton</p>
  </aside>

  <section class="clients">
    <div class="flag" role="img" aria-label="Faint flag decoration"></div>
    <h2>Tarrowby &amp; Quenell, L.L.C.,<br>representative clients:</h2>
    <ul class="client-list">
      <li>Brantock Alloys, Inc.</li>
      <li>Harborline Trust Bank</li>
      <li>Elmhurst Club of Princeton</li>
      <li>RK Solvent Company, Inc.</li>
      <li>Fernwood Realty</li>
      <li>Harlow Square Management, LLC</li>
      <li>Vossberg Chemical &amp; Mineral Corp.</li>
    </ul>
    <ul class="services">
      <li>Transacting business in energy and high-tech industries;</li>
      <li>Owning or developing land;</li>
      <li>Structuring corporate entities;</li>
      <li>Engaging in site planning and redevelopment, including re-use of historic or contaminated parcels;</li>
      <li>Facing environmental enforcement actions or litigation;</li>
      <li>Litigating business disputes.</li>
    </ul>
  </section>

  <aside class="sidebar">
    <div class="tab areas">AREAS OF PRACTICE:</div>
    <ul class="practice">
      <li>Environmental Law</li>
      <li>Land Use Law</li>
      <li>Zoning</li>
      <li>Redevelopment</li>
      <li>Corporate Law</li>
      <li>Complex Business</li>
      <li>Litigation</li>
    </ul>
    <div class="tab offices">OFFICE LOCATIONS:</div>
    <div class="office-box">
      <div class="city c1">PRINCETON, NJ</div>
      <div class="phone">(609) 555-0148</div>
      <div class="city c2">NEW YORK, NY</div>
      <div class="phone">(917) 555-0172</div>
    </div>
  </aside>

  <footer class="footer">
    <span>Business manager: Dana Mercer</span>
    <a href="#">dana@tarrowbyquenell.com</a>
  </footer>
</div>
</body>
</html>
```